Health insurance quote - Modularity made easy

Realization of the design of a responsive Web application allowing an individual to proceed to the pricing and online subscription of a complementary health (4 steps). The principle of this complementary health is the modularity of the person (s) of the patient (s) (general care, hospitalization, optics, dental, soft medicine) according to the needs of the patient. personalized for each member of the family (parents children). Attached you will find a document summarizing the steps of the project.
Updates
Faible participation designers
Target Market(s)
Individual Clientele Independent and Senior Workers
Industry/Entity Type
Health Insurance
Colors
Designer to choose colors to be used in the design.
Requirements
Must have
- Simple; Clear; Friendly; Playful; Modular The design must adapt to a responsive format (Web, Ipad, Iphone)
Nice to have
- The choice of needs to be both simple and detailed. With the possibility of modifying needs during pricing

```html
<!DOCTYPE html>
<html lang="fr">
<head>
<meta charset="utf-8">
<title>Tarification Complémentaire Santé</title>
<link href="https://fonts.googleapis.com/css2?family=Montserrat:wght@400;500;600;700&display=swap" rel="stylesheet">
<style>
:root{
  --navy:#0a3a8c;
  --blue:#0a9cf5;
  --ink:#1d2b4a;
  --text:#3a4150;
  --muted:#8f96a3;
  --line:#d9dde4;
  --pill:#f2f3f6;
  --header:#f6f7f9;
  --icon-bg:#b9bec8;
  --white:#fff;
}
*{box-sizing:border-box;margin:0;padding:0}
html,body{width:1200px;height:675px;overflow:hidden;background:var(--white);font-family:'Montserrat',sans-serif;color:var(--text)}
.app{position:relative;width:1200px;height:675px}
.abs{position:absolute}
.topbar{left:0;top:0;width:1200px;height:56px;background:var(--header)}
.brand{left:10px;top:14px;font-size:21px;font-weight:500;color:var(--ink)}
.page-title{left:0;width:1200px;top:17px;text-align:center;font-size:16px;font-weight:500;color:var(--ink);letter-spacing:.3px}
.avatar{left:1103px;top:10px;width:37px;height:37px;border-radius:50%;background:var(--navy)}
.caret{left:1150px;top:26px;border:4px solid transparent;border-top-color:#b6bbc4}
.sidebar{left:0;top:56px;width:62px;height:619px;background:var(--navy)}
.side-icon{left:19px;width:24px;height:24px}
.stepper-line{top:110px;height:1px;background:var(--line)}
.step{width:28px;height:28px;border-radius:50%;border:1px solid var(--line);background:var(--white);font-size:9px;display:flex;align-items:center;justify-content:center;color:var(--muted);top:96px}
.step.active{border:2px solid var(--blue);color:var(--blue)}
.step-label{top:133px;width:120px;text-align:center;font-size:9px;color:var(--muted)}
.step-label.active{color:var(--blue);font-weight:600}
.card{top:194px;width:468px;height:427px;border:1.5px solid #e3e6eb}
.photo{left:190px;top:38px;width:86px;height:86px;border-radius:50%;background:var(--pill);display:flex;align-items:center;justify-content:center}
.upload{left:0;width:466px;text-align:center;top:132px;font-size:9px;color:var(--blue)}
.upload-note{left:0;width:466px;text-align:center;top:146px;font-size:7px;color:var(--muted)}
.choice{top:206px;width:112px;height:25px;border-radius:13px;background:var(--pill);font-size:10.5px;font-weight:500;padding-left:19px;display:flex;align-items:center}
.radio{position:absolute;right:18px;top:6px;width:13px;height:13px;border-radius:50%;border:1px solid #c9ced6;background:var(--white)}
.radio.on::after{content:"";position:absolute;left:3px;top:3px;width:5px;height:5px;border-radius:50%;background:var(--blue)}
.field-label{font-size:10.5px;font-weight:500;color:var(--text)}
.input{width:189px;height:25px;border:1px solid #d3d7de;border-radius:13px;font-size:10px;color:#a9afba;padding-left:12px;display:flex;align-items:center}
.btn{height:25px;width:93px;border-radius:13px;background:var(--blue);color:var(--white);font-size:9px;font-weight:700;letter-spacing:.6px;display:flex;align-items:center;justify-content:center;top:388px}
.section-title{left:0;width:466px;text-align:center;top:27px;font-size:15px;font-weight:500;color:var(--blue)}
.row-icon{left:42px;width:32px;height:32px;border-radius:50%;background:var(--icon-bg);display:flex;align-items:center;justify-content:center}
.row{left:83px;width:326px;height:30px;border-radius:15px;background:var(--pill);font-size:13px;font-weight:500;color:#2f3542;padding-left:19px;display:flex;align-items:center}
.toggle{position:absolute;right:4px;top:5px;width:49px;height:20px;border-radius:10px;background:#e6e8ec}
.toggle::after{content:"";position:absolute;top:1px;right:3px;width:18px;height:18px;border-radius:50%;background:#b8bdc6}
.toggle.on::after{right:auto;left:3px;background:var(--blue)}
</style>
</head>
<body>
<div class="app">
  <header class="abs topbar"></header>
  <div class="abs brand">logo</div>
  <div class="abs page-title">Tarification Complémentaire Santé</div>
  <div class="abs avatar"></div>
  <div class="abs caret"></div>

  <nav class="abs sidebar"></nav>
  <svg class="abs side-icon" style="top:231px" viewBox="0 0 24 24" fill="#fff"><circle cx="12" cy="7" r="5"/><path d="M2 22c0-5 4-8 10-8s10 3 10 8z"/></svg>
  <svg class="abs side-icon" style="top:297px" viewBox="0 0 24 24" fill="#fff"><path d="M1 12C2 6 7 3 12 3s10 3 11 9c-1.5-1-3-1-4 0-1-1-3-1-4 0-1-1-3-1-4 0-1-1-3-1-4 0-1-1-3-1-4 0-1-1-2.5-1-4 0z"/><path d="M11.2 12h1.6v7a3 3 0 0 1-6 0h1.6a1.4 1.4 0 0 0 2.8 0z"/></svg>
  <svg class="abs side-icon" style="top:358px" viewBox="0 0 24 24" fill="none" stroke="#fff" stroke-width="3" stroke-linecap="round"><path d="M19 5a8 8 0 1 0 0 14"/><path d="M3 10h10M3 14h10"/></svg>
  <svg class="abs side-icon" style="top:421px" viewBox="0 0 24 24" fill="#fff"><path d="M22 2 2 10l6 3 10-8-8 9v7l4-5 4 3z"/></svg>

  <div class="abs stepper-line" style="left:408px;width:440px"></div>
  <div class="abs step active" style="left:380px">1</div>
  <div class="abs step" style="left:537px">2</div>
  <div class="abs step" style="left:691px">3</div>
  <div class="abs step" style="left:848px">4</div>
  <div class="abs step-label active" style="left:335px">Première étape</div>
  <div class="abs step-label" style="left:491px">Deuxième étape</div>
  <div class="abs step-label" style="left:645px">Troisième étape</div>
  <div class="abs step-label" style="left:801px">Quatrième étape</div>

  <section class="abs card" style="left:150px">
    <div class="abs photo">
      <svg width="24" height="20" viewBox="0 0 24 20" fill="#b9bec8"><path d="M8 1h8l2 3h4a2 2 0 0 1 2 2v12a2 2 0 0 1-2 2H2a2 2 0 0 1-2-2V6a2 2 0 0 1 2-2h4z"/><circle cx="12" cy="12" r="5" fill="#f2f3f6"/><circle cx="12" cy="12" r="3"/></svg>
    </div>
    <div class="abs upload">Télécharger votre photo de profil</div>
    <div class="abs upload-note">Résolution 150 x 150px et taille 1mo maximale</div>

    <div class="abs choice" style="left:31px">Femme<span class="radio on"></span></div>
    <div class="abs choice" style="left:178px">Homme<span class="radio"></span></div>
    <div class="abs choice" style="left:324px">Enfant<span class="radio"></span></div>

    <div class="abs field-label" style="left:31px;top:259px">Nom</div>
    <div class="abs field-label" style="left:247px;top:259px">Prénom</div>
    <div class="abs input" style="left:31px;top:276px">votre nom</div>
    <div class="abs input" style="left:247px;top:276px">votre prénom</div>

    <div class="abs field-label" style="left:31px;top:323px">Date de naissance</div>
    <div class="abs field-label" style="left:247px;top:323px">Régime d'assurance</div>
    <div class="abs input" style="left:31px;top:341px"></div>
    <div class="abs input" style="left:247px;top:341px">
      <svg style="position:absolute;right:12px;top:9px" width="8" height="6" viewBox="0 0 8 6" fill="none" stroke="#8f96a3" stroke-width="1.2"><path d="M1 1l3 3 3-3"/></svg>
    </div>

    <div class="abs btn" style="left:344px">VALIDER</div>
  </section>

  <section class="abs card" style="left:642px">
    <div class="abs section-title">Les renforts</div>

    <div class="abs row-icon" style="top:79px"><svg width="18" height="18" viewBox="0 0 18 18" fill="none" stroke="#fff" stroke-width="1.4"><path d="M9 1v16M4 4c3 1 7 1 10 0M5 8c2 2 6 0 8 2s-2 4-4 3-4 1-2 3"/></svg></div>
    <div class="abs row" style="top:80px">Soins généraux<span class="toggle on"></span></div>

    <div class="abs row-icon" style="top:120px"><svg width="18" height="18" viewBox="0 0 18 18" fill="none" stroke="#fff" stroke-width="1.6"><path d="M6.5 1h5v5.5H17v5h-5.5V17h-5v-5.5H1v-5h5.5z"/></svg></div>
    <div class="abs row" style="top:121px">Hospitalisation<span class="toggle"></span></div>

    <div class="abs row-icon" style="top:162px"><svg width="20" height="14" viewBox="0 0 20 14" fill="none" stroke="#fff" stroke-width="1.5"><path d="M1 7c4-7 14-7 18 0-4 7-14 7-18 0z"/><circle cx="10" cy="7" r="3"/></svg></div>
    <div class="abs row" style="top:163px">Optique<span class="toggle"></span></div>

    <div class="abs row-icon" style="top:204px"><svg width="16" height="18" viewBox="0 0 16 18" fill="none" stroke="#fff" stroke-width="1.4"><path d="M4 1c2 0 3 1 4 1s2-1 4-1 3 2 3 5-2 4-2 7-1 4-2 4-1-5-3-5-2 5-3 5-2-1-2-4-2-4-2-7 1-5 3-5z"/></svg></div>
    <div class="abs row" style="top:205px">Dentaire<span class="toggle on"></span></div>

    <div class="abs row-icon" style="top:246px"><svg width="14" height="20" viewBox="0 0 14 20" fill="none" stroke="#fff" stroke-width="1.4"><path d="M2 7a5 5 0 0 1 10 0c0 4-4 5-4 8a3 3 0 0 1-5 2"/><path d="M5 7a2 2 0 0 1 4 0c0 2-2 2-2 4"/></svg></div>
    <div class="abs row" style="top:247px">Auditif<span class="toggle"></span></div>

    <div class="abs row-icon" style="top:288px"><svg width="18" height="18" viewBox="0 0 18 18" fill="none" stroke="#fff" stroke-width="1.4"><path d="M1 9h16a8 8 0 0 1-16 0zM9 9l6-7M8 12h2"/></svg></div>
    <div class="abs row" style="top:289px">Médicines douces<span class="toggle"></span></div>

    <div class="abs btn" style="left:316px">TERMINER</div>
  </section>
</div>
</body>
</html>
```